IRON SASH VIGOUR CERTIFICATE

Carrowby Hapkido Inc is wanting to introduce a fitness system based upon certificates reflecting rank; White - Yellow - Blue - Red - Black.

The Certificate "MUST" have on it "IRON SASH VIGOUR"

The Certificate "MUST" have a martial arts theme!

The Certificate "MUST" reflect the fitness requirements for each rank.

The colour scheme for each Certificate "MUST" reflect the belt rank

The Certificate must include at least one martial arts graphic / motif

The certificate must have the Carrowby HKD LOGO

We will need a certificate template that can be for all levels but reflect the rank and fitness level. The certificate can be either traditional or modern style but must reflect a martial art themes. The certificate must have the Carrowby Hapkido logo incorporated into the certificate with signature space for senior instructors Dan Pellow & Sorna Vick-Pellow. The certificates should be eye catching and exciting to look at. It should bold and incorporate martial art motifs etc The fitness requirements are not onerous and the certificate system is created to incentivise physical activity and correct technique rather than creating an impossible standards only Olympians can achieve. The majority of our students are upper primary and lower secondary from 11yr-15yrs. Certificate should be youthful but not silly. The certificate template will be reproduced for each colour belt.White = 10 push ups 10 Sit ups 10 squats 10 Jumping Jacks 20 sec plank 400m continuous run Demonstrate beginner stretching techniqueYellow = 20 push ups 20 sit ups 20 squats 20 Jumping Jacks 40 Sec plank 800m continuous run Demonstrate intermediate stretching techniqueBlue = 30 push ups 30 sit ups 30 squats 30 Jumping Jacks 60 Sec plank 1200m continuous run Demonstrate intermediate stretching techniqueRed = 40 push ups 40 sit ups 40 squats 40 Jumping Jacks 75sec plank 1600m run Demonstrate advanced stretching techniqueBlack = 50 push ups 50 sit ups 50 squats 50 Jumping jacks 90 sec planks 2000m continuous run Demonstrate advanced stretching technique
Updates

HI Designers, Please go for modern and professionals. Several designs have used traditional motifs of water dragons or lattice bordering. This looks old school. Please do not use martial art silhouettes as it looks amateur. Definately looking for upmarket high quality presentations.

Logo Text

IRON SASH VIGOUR

Font styles to use
Decorative

Colors

Designer to choose colors to be used in the design.

Requirements
Must have
• This will be a template foe all coloured ranks of fitness, Be bold, memorable, should be themed to martial arts etc

```html
<!DOCTYPE html>
<html lang="en">
<head>
<meta charset="utf-8">
<title>Iron Sash Vigour Certificates</title>
<link rel="stylesheet" href="https://fonts.googleapis.com/css2?family=Cinzel:wght@400;600&family=Montserrat:wght@400;600;700;900&display=swap">
<style>
  :root {
    --ink: #111111;
    --navy: #2a2f3d;
    --paper: #ffffff;
    --paper-shade: #eceef1;
    --red: #e3202a;
    --yellow: #e0b12a;
    --blue: #1f35d6;
    --grey: #cfd1d4;
    --black: #1a1a1a;
  }
  * { margin: 0; padding: 0; box-sizing: border-box; }
  html, body { width: 794px; height: 1200px; overflow: hidden; background: var(--paper); }
  .sheet { position: relative; width: 794px; height: 1200px; background: var(--paper); }

  .cert {
    position: absolute;
    width: 700px; height: 542px;
    transform-origin: 0 0;
    background: radial-gradient(ellipse at 55% 45%, var(--paper) 30%, var(--paper-shade) 100%);
    box-shadow: 0 6px 18px rgba(0,0,0,.28);
    overflow: hidden;
    font-family: "Montserrat", sans-serif;
    color: var(--ink);
  }
  .cert--main { left: 40px; top: 42px; }
  .cert--black { left: 36px; top: 602px; transform: scale(.48); }
  .cert--yellow { left: 402px; top: 610px; transform: scale(.48); }
  .cert--white { left: 38px; top: 889px; transform: scale(.48); }
  .cert--blue { left: 402px; top: 889px; transform: scale(.48); }

  .rank-red { --accent: var(--red); --title: var(--red); }
  .rank-black { --accent: var(--black); --title: var(--ink); }
  .rank-yellow { --accent: var(--yellow); --title: var(--yellow); }
  .rank-white { --accent: var(--grey); --title: var(--ink); }
  .rank-blue { --accent: var(--blue); --title: var(--blue); }

  .frame { position: absolute; inset: 0; width: 700px; height: 542px; }

  .hero-art {
    position: absolute; left: 22px; top: 22px; width: 240px; height: 400px;
    border-radius: 45% 55% 35% 50%;
    background: linear-gradient(150deg, var(--navy) 0%, var(--accent) 55%, rgba(255,255,255,0) 100%);
    opacity: .8;
  }

  .heading { position: absolute; text-align: center; }
  .heading__top { left: 300px; width: 270px; top: 58px; font-size: 27px; font-weight: 400; letter-spacing: 1px; }
  .heading__main { left: 285px; width: 300px; top: 84px; font-size: 62px; font-weight: 900; letter-spacing: -1px; line-height: 1; }

  .recipient {
    position: absolute; left: 221px; top: 180px; width: 420px;
    text-align: center; font-family: "Cinzel", serif; font-size: 38px; letter-spacing: 2px;
    padding-bottom: 6px; border-bottom: 2px solid var(--ink);
  }

  .rank {
    position: absolute; left: 221px; top: 262px; width: 420px; text-align: center;
    font-size: 33px; font-weight: 700; color: var(--title); letter-spacing: -.5px;
  }
  .requirements {
    position: absolute; left: 221px; top: 310px; width: 420px; text-align: center;
    font-size: 11px; line-height: 1.3;
  }

  .signature {
    position: absolute; top: 415px; width: 184px; text-align: center;
    border-top: 2px solid var(--ink); padding-top: 7px;
  }
  .signature--first { left: 228px; }
  .signature--second { left: 432px; }
  .signature__name { font-size: 14px; font-weight: 700; text-transform: uppercase; letter-spacing: -.2px; white-space: nowrap; }
  .signature__role { font-size: 12.5px; letter-spacing: .3px; margin-top: 1px; }

  .club-mark {
    position: absolute; left: 45px; top: 405px; width: 114px; height: 114px;
    border-radius: 50%; background: var(--navy);
    display: flex; align-items: center; justify-content: center; text-align: center;
  }
  .club-mark__name {
    color: var(--paper); font-weight: 700; font-size: 13px; line-height: 1.2;
    text-transform: uppercase; letter-spacing: .5px; padding: 0 10px;
  }
</style>
</head>
<body>
<svg width="0" height="0" style="position:absolute" aria-hidden="true">
  <defs>
    <symbol id="corner-frame" viewBox="0 0 700 542">
      <polygon points="410,0 700,0 700,542 430,542 610,505 668,430 680,290 655,150 565,22" fill="var(--accent)"/>
      <polygon points="450,0 700,0 700,542 475,542 628,515 685,435 695,290 672,140 592,15" fill="var(--navy)"/>
      <polygon points="610,0 700,0 700,80 650,45" fill="var(--accent)" opacity=".9"/>
      <polygon points="700,400 700,542 620,542 685,480" fill="var(--accent)" opacity=".9"/>
    </symbol>
  </defs>
</svg>

<main class="sheet">

  <section class="cert cert--main rank-red">
    <svg class="frame" viewBox="0 0 700 542" aria-hidden="true"><use href="#corner-frame"/></svg>
    <div class="hero-art" role="img" aria-label="Illustration of a martial artist performing a high kick with red flames"></div>
    <p class="heading heading__top">IRON SASH</p>
    <p class="heading heading__main">VIGOUR</p>
    <p class="recipient">Name Lastname</p>
    <p class="rank">RED BELT</p>
    <p class="requirements">40 push ups, 40 sit ups, 40 squats, 40 Jumping Jacks, 75sec plank,<br>1600m run, Demonstrate advanced stretching technique</p>
    <div class="signature signature--first"><p class="signature__name">Dan Pellow</p><p class="signature__role">Senior Instructor</p></div>
    <div class="signature signature--second"><p class="signature__name">Sorna Vick-Pellow</p><p class="signature__role">Senior Instructor</p></div>
    <div class="club-mark"><span class="club-mark__name">Carrowby Hapkido</span></div>
  </section>

  <section class="cert cert--black rank-black">
    <svg class="frame" viewBox="0 0 700 542" aria-hidden="true"><use href="#corner-frame"/></svg>
    <div class="hero-art" role="img" aria-label="Illustration of a martial artist performing a high kick with black flames"></div>
    <p class="heading heading__top">IRON SASH</p>
    <p class="heading heading__main">VIGOUR</p>
    <p class="recipient">Name Lastname</p>
    <p class="rank">BLACK BELT</p>
    <p class="requirements">50 push ups, 50 sit ups, 50 squats, 50 Jumping jacks, 90 sec planks,<br>2000m continuous run, Demonstrate advanced stretching technique</p>
    <div class="signature signature--first"><p class="signature__name">Dan Pellow</p><p class="signature__role">Senior Instructor</p></div>
    <div class="signature signature--second"><p class="signature__name">Sorna Vick-Pellow</p><p class="signature__role">Senior Instructor</p></div>
    <div class="club-mark"><span class="club-mark__name">Carrowby Hapkido</span></div>
  </section>

  <section class="cert cert--yellow rank-yellow">
    <svg class="frame" viewBox="0 0 700 542" aria-hidden="true"><use href="#corner-frame"/></svg>
    <div class="hero-art" role="img" aria-label="Illustration of a martial artist performing a high kick with yellow flames"></div>
    <p class="heading heading__top">IRON SASH</p>
    <p class="heading heading__main">VIGOUR</p>
    <p class="recipient">Name Lastname</p>
    <p class="rank">YELLOW BELT</p>
    <p class="requirements">20 push ups, 20 sit ups, 20 squats, 20 Jumping Jacks, 40 Sec plank,<br>800m continuous run, Demonstrate intermediate stretching technique</p>
    <div class="signature signature--first"><p class="signature__name">Dan Pellow</p><p class="signature__role">Senior Instructor</p></div>
    <div class="signature signature--second"><p class="signature__name">Sorna Vick-Pellow</p><p class="signature__role">Senior Instructor</p></div>
    <div class="club-mark"><span class="club-mark__name">Carrowby Hapkido</span></div>
  </section>

  <section class="cert cert--white rank-white">
    <svg class="frame" viewBox="0 0 700 542" aria-hidden="true"><use href="#corner-frame"/></svg>
    <div class="hero-art" role="img" aria-label="Illustration of a martial artist performing a high kick with light grey flames"></div>
    <p class="heading heading__top">IRON SASH</p>
    <p class="heading heading__main">VIGOUR</p>
    <p class="recipient">Name Lastname</p>
    <p class="rank">WHITE BELT</p>
    <p class="requirements">10 push ups, 10 Sit ups, 10 squats, 10 Jumping Jacks, 20 sec plank<br>400m continuous run, Demonstrate beginner stretching technique</p>
    <div class="signature signature--first"><p class="signature__name">Dan Pellow</p><p class="signature__role">Senior Instructor</p></div>
    <div class="signature signature--second"><p class="signature__name">Sorna Vick-Pellow</p><p class="signature__role">Senior Instructor</p></div>
    <div class="club-mark"><span class="club-mark__name">Carrowby Hapkido</span></div>
  </section>

  <section class="cert cert--blue rank-blue">
    <svg class="frame" viewBox="0 0 700 542" aria-hidden="true"><use href="#corner-frame"/></svg>
    <div class="hero-art" role="img" aria-label="Illustration of a martial artist performing a high kick with blue flames"></div>
    <p class="heading heading__top">IRON SASH</p>
    <p class="heading heading__main">VIGOUR</p>
    <p class="recipient">Name Lastname</p>
    <p class="rank">BLUE BELT</p>
    <p class="requirements">30 push ups, 30 sit ups, 30 squats, 30 Jumping Jacks 60 Sec plank,<br>1200m continuous run, Demonstrate intermediate stretching technique</p>
    <div class="signature signature--first"><p class="signature__name">Dan Pellow</p><p class="signature__role">Senior Instructor</p></div>
    <div class="signature signature--second"><p class="signature__name">Sorna Vick-Pellow</p><p class="signature__role">Senior Instructor</p></div>
    <div class="club-mark"><span class="club-mark__name">Carrowby Hapkido</span></div>
  </section>

</main>
</body>
</html>
```